Adlinks Landing Page - DESIGN ONLY! PSD File

BACKGROUND:
Our website www.trailkit.com.au (running on Storlane) has a range of outdoor equipment being sold online. One of the products we specialize in is generators.
We are after a content landing page designed for Bluefin Adlinks to link to. This page should be focused on converting customers to sales as most customers at this stage of buying are ready to buy. We would like this page to focus on a combination of a professional graphic design and some text. The way it is laid out is open to your own experience, we just want it to look professional and have the right info for customers to convert.
THE BRIEF:
The page will include the range of products in the generator category that can be found here:
http://www.trailkit.com.au/generators.html
This page should include all the products within this category and should fit into to the color scheme and look of the website.
Most focus on the product should be placed in this order of priority, with special focus on the first two:
1. 2kva RRP: $1099 down to $499
2. 3.5kva RRP: $1399 down to $780
3. 3.5kva electric start RRP: $1599 down to $890
4. 4.4kva RRP: $1899 down to $950 (not currently listed, images will be provided soon)
5. 5kva RRP: $1999 down to $1150
The page can include a variety of graphic design, text and hyperlinks (or image clickable links), so please take this into account when making the graphics design.
The page must be discount oriented and include prices of each product as well as its original RRP price (crossed out), possible 'sale' graphics, and 'buy now' buttons linking to the product.
An example area this should fit within is the the column the products are on this page:
Other notes:
Our prices are truly bargains and the lowest in the market, so don't be afraid to express that in the design; texts like "Massive Sale" , "Priced to Clear Out" , "Won't Last Long at this Price"
Product images can be grabbed off the products here:
Deliverable will be a PSD file of the finished design.
We need these contact numbers included somewhere on this page:
NSW/ACT: 02 8555 0142
VIC/TAS: 03 9555 0176
SA: 08 7555 0193
NT/WA: 08 85550127

```html
<!DOCTYPE html>
<html lang="en">
<head>
<meta charset="utf-8">
<title>Generators – TrailKit</title>
<link rel="stylesheet" href="https://fonts.googleapis.com/css2?family=Arimo:wght@400;700&family=Roboto:wght@400;500;700&family=Noto+Serif&display=swap">
<style>
:root{
  --earth:#c98542;
  --earth-dark:#a9652d;
  --nav-top:#4a4a4a;
  --nav-bottom:#222;
  --nav-line:#5c5c5c;
  --nav-active:#e6e08a;
  --page:#ffffff;
  --ink:#1b1b1b;
  --rule:#2b2b2b;
  --link-green:#8cbd2a;
  --accent-red:#e53a43;
  --price-green:#13a55a;
  --ribbon:#b3261c;
  --ribbon-dark:#8a1a12;
  --gold:#e9b722;
  --card-line:#d4d4d4;
  --product-red:#d9312c;
}
*{box-sizing:border-box;margin:0;padding:0}
html,body{width:1200px;height:959px;overflow:hidden}
body{position:relative;font-family:"Arimo",Arial,sans-serif;color:var(--ink)}
.backdrop{position:absolute;inset:0;background:radial-gradient(circle at 30% 20%,#d69352,var(--earth) 50%,var(--earth-dark))}
.brand{position:absolute;left:102px;top:26px;font:700 30px "Arimo",sans-serif;color:#1b1b1b;display:flex;align-items:center;gap:8px}
.brand-dot{width:14px;height:14px;background:#1b1b1b}
.welcome{position:absolute;left:459px;top:24px;font-size:12px;line-height:21px;color:#f5e6c8}
.welcome a,.cart a{color:var(--link-green)}
.cart-icon{position:absolute;left:674px;top:26px}
.cart{position:absolute;left:717px;top:24px;font-size:12px;line-height:21px;color:#f5e6c8}
.sheet{position:absolute;left:87px;top:74px;width:1049px;height:885px;background:var(--page)}
.nav{position:absolute;left:87px;top:74px;width:1049px;height:42px;background:linear-gradient(var(--nav-top),var(--nav-bottom));display:flex}
.search{width:285px;display:flex;align-items:center;padding-left:13px;gap:4px;border-right:1px solid var(--nav-line)}
.search-field{width:221px;height:22px;background:#fff;border:1px solid #999;display:flex;align-items:center;gap:5px;padding-left:5px;font-size:13px;color:#222}
.search-go{width:35px;height:22px;background:linear-gradient(#f2f2f2,#c9c9c9);border:1px solid #888;font:700 12px "Arimo",sans-serif;display:flex;align-items:center;justify-content:center}
.nav-item{display:flex;align-items:center;justify-content:center;font:700 12px "Arimo",sans-serif;color:#fff;border-right:1px solid var(--nav-line)}
.nav-item.active{color:var(--nav-active)}
.nav-item:last-child{border-right:none}
.crumbs{position:absolute;left:98px;top:127px;font-size:11px;color:var(--ink)}
.crumbs a{color:var(--link-green)}
.box{position:absolute;left:98px;width:265px;border:1px solid #d8d8d8;background:#fff}
.categories{top:153px;height:476px}
.specials{top:646px;height:330px}
.box-title{display:flex;align-items:center;gap:6px;margin:12px 0 0 12px;font:700 17px "Arimo",sans-serif;color:#000}
.cat-list{list-style:none;margin:1px 12px 0 13px}
.cat-list li{height:30.8px;border-bottom:1px dotted var(--rule);display:flex;align-items:center;padding-left:8px;font-size:14.5px;color:#666}
.cat-list li::before{content:"";width:5px;height:5px;border-radius:50%;background:#444;margin-right:11px}
.special-item{position:absolute;width:110px}
.special-thumb{height:75px;width:96px;margin-left:6px}
.special-name{margin-top:32px;font:700 12.5px/17px "Arimo",sans-serif;color:#1f2c47;text-decoration:underline}
.special-price{margin-top:8px;font:700 13px "Arimo",sans-serif}
.page-title{position:absolute;left:374px;top:156px;font:400 21px "Arimo",sans-serif;color:#1e2a3a}
.promo{position:absolute;left:431px;top:188px;width:519px;height:108px}
.promo-art{position:absolute;inset:0;border-radius:6px;background:linear-gradient(90deg,var(--gold) 0,var(--gold) 19%,var(--ribbon) 21%,var(--ribbon-dark))}
.promo-text{position:absolute;left:118px;top:37px;font:400 25px "Noto Serif",serif;color:#fff;white-space:nowrap}
.card{position:absolute;border:1px solid var(--card-line);border-radius:8px;background:linear-gradient(#fff 40%,#ececec);box-shadow:0 1px 3px rgba(0,0,0,.12)}
.card-title{position:absolute;font:500 17px/22px "Roboto",sans-serif;color:#222;letter-spacing:.4px}
.card-title em{font-style:normal;color:var(--accent-red)}
.card.small .card-title{font-size:14px;line-height:17px;font-weight:500}
.product-shot{position:absolute;border-radius:10px}
.regular{position:absolute;font:400 12.5px "Roboto",sans-serif;color:#333}
.was{font:400 12.5px "Roboto",sans-serif;color:#333;text-decoration:line-through}
.special-label{position:absolute;font:500 14px "Roboto",sans-serif;color:var(--accent-red)}
.now{position:absolute;font:500 24px "Roboto",sans-serif;color:var(--price-green)}
.buy{position:absolute;width:94px;height:33px;background:var(--accent-red);border-radius:3px;color:#fff;font:500 14.5px "Roboto",sans-serif;display:flex;align-items:center;justify-content:center}
.contacts{position:absolute;left:388px;top:920px;width:717px;display:flex;justify-content:space-between;font:400 12.5px "Roboto",sans-serif;color:#333}
.contacts b{font-weight:500;color:#222}
</style>
</head>
<body>
<div class="backdrop" role="img" aria-label="Cracked dry earth texture background"></div>

<div class="brand"><span class="brand-dot"></span>TrailKit</div>
<p class="welcome">Welcome! Click <a>here</a> to log<br>in or create an account.</p>
<svg class="cart-icon" width="34" height="30" viewBox="0 0 34 30" aria-hidden="true"><path d="M2 10 L26 4 L32 20 L10 27 Z" fill="#2b7fd1"/><path d="M6 10 L24 5 L22 0 L14 2 Z" fill="#f2c230"/></svg>
<p class="cart">Shopping Cart<br>now in your cart <a>0 items</a></p>

<div class="sheet"></div>
<nav class="nav">
  <div class="search">
    <div class="search-field"><svg width="13" height="13" viewBox="0 0 13 13"><circle cx="5" cy="5" r="4" fill="none" stroke="#333" stroke-width="1.6"/><line x1="8" y1="8" x2="12" y2="12" stroke="#333" stroke-width="2"/></svg>Search entire store here...</div>
    <div class="search-go">Go</div>
  </div>
  <div class="nav-item active" style="width:146px">HOME PAGE</div>
  <div class="nav-item" style="width:172px">NEW PRODUCTS</div>
  <div class="nav-item" style="width:135px">SPECIALS</div>
  <div class="nav-item" style="width:153px">MY ACCOUNT</div>
  <div class="nav-item" style="width:158px">CONTACT US</div>
</nav>

<p class="crumbs"><a>Home</a> / <b>Generators</b></p>

<aside class="box categories">
  <h2 class="box-title"><svg width="16" height="13" viewBox="0 0 16 13"><path d="M1 5h14l-2 8H3z" fill="#9aa3ad"/><path d="M4 5 8 1l4 4" fill="none" stroke="#9aa3ad" stroke-width="1.5"/></svg>CATEGORIES</h2>
  <ul class="cat-list">
    <li>Camper Trailers</li><li>Camping &amp; Outdoors</li><li>Awnings</li><li>Tents</li>
    <li>Carvanning &amp; 4WD</li><li>Jacks</li><li>Winches</li><li>Generators</li>
    <li>Inverters &amp; Regulators</li><li>Lighting</li><li>Refrigeration</li>
    <li>Fixed Solar Panels</li><li>Portable Solar Panels</li><li>Solar</li>
  </ul>
</aside>

<aside class="box specials">
  <h2 class="box-title"><svg width="16" height="13" viewBox="0 0 16 13"><path d="M1 5h14l-2 8H3z" fill="#9aa3ad"/><path d="M4 5 8 1l4 4" fill="none" stroke="#9aa3ad" stroke-width="1.5"/></svg>SPECIALS</h2>
  <div class="special-item" style="left:17px;top:58px">
    <div class="special-thumb" role="img" aria-label="4WD winch with synthetic rope" style="background:radial-gradient(#6a7a9a,#cfd3da 70%,#fff)"></div>
    <p class="special-name">4WD Synthetic Rope 12000lbs Winch</p>
    <p class="special-price">$599.00</p>
  </div>
  <div class="special-item" style="left:138px;top:58px">
    <div class="special-thumb" role="img" aria-label="Portable fridge freezer" style="background:linear-gradient(#e9e9e9,#bfbfbf)"></div>
    <p class="special-name">Coolvara 80L Portable Fridge Freezer</p>
    <p class="special-price">$579.00</p>
  </div>
</aside>

<h1 class="page-title">Generators</h1>

<div class="promo">
  <div class="promo-art" role="img" aria-label="Gold satisfaction guarantee seal beside a red ribbon banner"></div>
  <p class="promo-text">Lowest Prices in the market</p>
</div>

<article class="card" style="left:388px;top:320px;width:351px;height:260px">
  <h3 class="card-title" style="left:20px;top:15px">Silent <em>2kVA</em> Pure Sine Wave<br>Inverter Generator</h3>
  <div class="product-shot" role="img" aria-label="Red 2kVA inverter generator" style="left:25px;top:73px;width:147px;height:146px;background:radial-gradient(circle at 55% 45%,var(--product-red),#a81e1a 60%,#f4f4f4 72%)"></div>
  <p class="regular" style="left:213px;top:72px">Regular Price</p>
  <p class="was" style="position:absolute;left:213px;top:96px">$1099</p>
  <p class="special-label" style="left:213px;top:130px">Special Price</p>
  <p class="now" style="left:213px;top:154px">$499</p>
  <a class="buy" style="left:210px;top:195px">Buy Now</a>
</article>

<article class="card" style="left:754px;top:320px;width:351px;height:260px">
  <h3 class="card-title" style="left:20px;top:15px">Silent <em>3.5kVA</em> Pure Sine Wave<br>Inverter Generator</h3>
  <div class="product-shot" role="img" aria-label="Red 3.5kVA inverter generator" style="left:25px;top:73px;width:147px;height:146px;background:radial-gradient(circle at 55% 45%,var(--product-red),#a81e1a 60%,#f4f4f4 72%)"></div>
  <p class="regular" style="left:213px;top:72px">Regular Price</p>
  <p class="was" style="position:absolute;left:213px;top:96px">$1399</p>
  <p class="special-label" style="left:213px;top:130px">Special Price</p>
  <p class="now" style="left:213px;top:154px">$780</p>
  <a class="buy" style="left:210px;top:195px">Buy Now</a>
</article>

<article class="card small" style="left:388px;top:591px;width:234px;height:314px">
  <h3 class="card-title" style="left:16px;top:14px">Silent <em>3.5kVA</em> Pure Sine<br>Wave Inverter Generator<br>Electric Start + Remote</h3>
  <div class="product-shot" role="img" aria-label="Red 3.5kVA electric start generator" style="left:48px;top:80px;width:135px;height:120px;background:radial-gradient(circle at 50% 50%,var(--product-red),#b0231e 58%,#f4f4f4 72%)"></div>
  <p class="regular" style="left:16px;top:220px">Regular Price &nbsp;<span class="was">$1599</span></p>
  <p class="special-label" style="left:15px;top:249px">Special Price</p>
  <p class="now" style="left:15px;top:272px">$890</p>
  <a class="buy" style="left:123px;top:256px">Buy Now</a>
</article>

<article class="card small" style="left:630px;top:591px;width:234px;height:314px">
  <h3 class="card-title" style="left:16px;top:14px">Silent <em>4.4kVA</em> Pure Sine<br>Wave Inverter Generator<br>Electric Start + Remote</h3>
  <div class="product-shot" role="img" aria-label="Red 4.4kVA electric start generator" style="left:48px;top:80px;width:135px;height:120px;background:radial-gradient(circle at 50% 50%,var(--product-red),#b0231e 58%,#f4f4f4 72%)"></div>
  <p class="regular" style="left:16px;top:220px">Regular Price &nbsp;<span class="was">$1899</span></p>
  <p class="special-label" style="left:15px;top:249px">Special Price</p>
  <p class="now" style="left:15px;top:272px">$950</p>
  <a class="buy" style="left:123px;top:256px">Buy Now</a>
</article>

<article class="card small" style="left:871px;top:591px;width:234px;height:314px">
  <h3 class="card-title" style="left:16px;top:14px">Silent <em>5kVA</em> Pure Sine<br>Wave Inverter Generator<br>Electric Start + Remote</h3>
  <div class="product-shot" role="img" aria-label="Black and red 5kVA electric start generator" style="left:50px;top:80px;width:130px;height:126px;background:linear-gradient(90deg,#222 55%,var(--product-red) 55%)"></div>
  <p class="regular" style="left:16px;top:220px">Regular Price &nbsp;<span class="was">$1999</span></p>
  <p class="special-label" style="left:15px;top:249px">Special Price</p>
  <p class="now" style="left:15px;top:272px">$1150</p>
  <a class="buy" style="left:123px;top:256px">Buy Now</a>
</article>

<p class="contacts">
  <span><b>NSW/ACT:</b> 02 8555 0142</span>
  <span><b>VIC/TAS:</b> 03 9555 0176</span>
  <span><b>SA:</b> 08 7555 0193</span>
  <span><b>NT/WA:</b> 08 85550127</span>
</p>
</body>
</html>
```